New Signage Design Project

Real estate company looking for signage, PowerPoint and stationery branding. Signs will be placed in front of homes and other properties being sold

Name of company is Tern Haven, LLC

Requirements
Must have
• Name of company - Tern Haven, LLC

```html
<!DOCTYPE html>
<html lang="en">
<head>
<meta charset="utf-8">
<title>Tern Haven, LLC — Sold Sign</title>
<link rel="stylesheet" href="https://fonts.googleapis.com/css2?family=Montserrat:wght@800&display=swap">
<style>
  :root {
    --slate: #222e2f;
    --paper: #ffffff;
    --sage: #84a4a3;
    --coral: #e25160;
  }
  html, body {
    margin: 0;
    padding: 0;
    width: 1200px;
    height: 900px;
    overflow: hidden;
    background: var(--slate);
  }
  .sign {
    display: block;
    width: 1200px;
    height: 900px;
  }
  .sign__base { fill: var(--slate); }
  .sign__banner { fill: var(--paper); }
  .sign__headline {
    font-family: "Montserrat", sans-serif;
    font-weight: 800;
    font-size: 306px;
    fill: var(--slate);
  }
  .stripe--sage { fill: var(--sage); }
  .stripe--coral { fill: var(--coral); }
  .brand__dot { fill: var(--coral); }
  .brand__name {
    font-family: "Montserrat", sans-serif;
    font-weight: 800;
    fill: var(--paper);
  }
  .brand__name--main { font-size: 92px; }
  .brand__name--suffix { font-size: 56px; }
</style>
</head>
<body>
<svg class="sign" viewBox="0 0 1200 900" xmlns="http://www.w3.org/2000/svg">
  <defs>
    <linearGradient id="fadeStripe" x1="1195" y1="488" x2="790" y2="900" gradientUnits="userSpaceOnUse">
      <stop offset="0" stop-color="#ffffff"/>
      <stop offset="0.45" stop-color="#6a6e72"/>
      <stop offset="1" stop-color="#222e2f"/>
    </linearGradient>
  </defs>

  <rect class="sign__base" x="0" y="0" width="1200" height="900"/>

  <polygon class="sign__banner" points="0,101.6 1200,101.6 970,376 0,376"/>
  <text class="sign__headline" x="86" y="343" textLength="850" lengthAdjust="spacingAndGlyphs">SOLD</text>

  <polygon class="stripe stripe--sage" points="1200,101.6 1200,172 994,418 935,418"/>
  <polygon class="stripe stripe--coral" points="1200,231 1200,314 966,597 898,597"/>
  <polygon class="stripe stripe--fade" fill="url(#fadeStripe)" points="1115,488 1195,488 850,900 784,900"/>

  <g class="brand">
    <circle class="brand__dot" cx="150" cy="540" r="60"/>
    <text class="brand__name brand__name--main" x="88" y="720">TERN HAVEN,</text>
    <text class="brand__name brand__name--suffix" x="92" y="800">LLC</text>
  </g>
</svg>
</body>
</html>
```